Bright Harbor Concierge

I need a website developed for our travel concierge service. I'm looking to be able to collect information and have the information collected directed to a inbox. I would also like to me able to manage the updates to the website myself. I also would like a mobile version of the website to be included. Our services include assistance with Bachelor Parties, Bachelorette Parties and Medical Tourism. We provide custom packages that include Airport Transportation, Lodging, Bilingual guides and any other special needs identified by our clients.
Industry/Entity Type
Travel
Coding
Coded - Design and coding required
Number of Pages Required
4 page
Look and feel

```html
<!DOCTYPE html>
<html lang="en">
<head>
<meta charset="utf-8">
<title>Bright Harbor Concierge — Desktop and Mobile Home</title>
<link rel="stylesheet" href="https://fonts.googleapis.com/css2?family=Libre+Baskerville:ital,wght@0,400;0,700;1,400&family=Montserrat:ital,wght@0,400;0,600;0,700;1,400&display=swap">
<style>
:root{
  --stage:#222222;
  --black:#000000;
  --panel:#262626;
  --gold:#f2b51c;
  --orange:#f0a020;
  --cyan:#00aeef;
  --blue:#1a5ea8;
  --navy:#16509a;
  --teal:#5db4c0;
  --red:#c93a3a;
  --white:#ffffff;
  --muted:#bdbdbd;
  --field:#3a3a3a;
  --serif:'Libre Baskerville', Georgia, serif;
  --sans:'Montserrat', Arial, sans-serif;
  --photo-pool:radial-gradient(ellipse at 30% 70%,rgba(64,140,190,.9),transparent 55%),radial-gradient(ellipse at 55% 35%,rgba(214,150,120,.85),transparent 50%),radial-gradient(ellipse at 85% 40%,rgba(120,80,60,.8),transparent 45%),linear-gradient(110deg,#2f6f9a 0%,#5a6f8a 30%,#a07868 55%,#7a5a4a 75%,#3d6a88 100%);
  --photo-bachelor:radial-gradient(ellipse at 35% 30%,rgba(200,120,110,.7),transparent 50%),radial-gradient(ellipse at 75% 25%,rgba(60,140,120,.6),transparent 45%),linear-gradient(180deg,#3a2a40 0%,#7a2f3c 55%,#d23c3c 100%);
  --photo-bachelorette:radial-gradient(ellipse at 45% 30%,rgba(220,190,170,.75),transparent 50%),linear-gradient(180deg,#9ab0cc 0%,#5a82b2 55%,#2f64a8 100%);
  --photo-medical:radial-gradient(ellipse at 60% 35%,rgba(170,150,160,.8),transparent 50%),linear-gradient(180deg,#8e8a96 0%,#a25460 55%,#d23c3c 100%);
  --photo-airport:radial-gradient(ellipse at 30% 50%,rgba(220,150,160,.7),transparent 35%),radial-gradient(ellipse at 60% 20%,rgba(240,220,90,.55),transparent 30%),linear-gradient(90deg,#c6c9cf,#8c939e 60%,#5c6470);
  --photo-lodge:radial-gradient(ellipse at 35% 30%,rgba(170,200,230,.85),transparent 40%),radial-gradient(ellipse at 75% 70%,rgba(110,70,50,.85),transparent 45%),linear-gradient(90deg,#5f8a4a,#8aa8c8 50%,#6a5040);
  --photo-tour:radial-gradient(ellipse at 40% 25%,rgba(230,225,215,.8),transparent 40%),radial-gradient(ellipse at 50% 65%,rgba(220,90,120,.55),transparent 30%),linear-gradient(180deg,#9ec0e0 0%,#b8b4a8 45%,#7aa85a 100%);
  --photo-bar:radial-gradient(ellipse at 40% 40%,rgba(220,150,110,.8),transparent 45%),linear-gradient(135deg,#a0401a,#4a1e12 60%,#2a1a14);
  --photo-toast:radial-gradient(ellipse at 50% 40%,rgba(210,170,150,.7),transparent 45%),linear-gradient(135deg,#34445e,#7a6a6a 60%,#9a7a5a);
  --photo-house:radial-gradient(ellipse at 20% 30%,rgba(220,160,120,.75),transparent 35%),radial-gradient(ellipse at 70% 60%,rgba(40,30,30,.9),transparent 40%),radial-gradient(ellipse at 40% 75%,rgba(180,40,40,.6),transparent 30%),linear-gradient(135deg,#8a5a32,#4a2a1e 55%,#7a4a30);
  --photo-club:radial-gradient(ellipse at 50% 30%,rgba(200,200,220,.45),transparent 40%),linear-gradient(160deg,#1a2436,#3a4a68 60%,#6a5a6a);
  --photo-confetti:radial-gradient(ellipse at 50% 60%,rgba(200,160,190,.7),transparent 45%),linear-gradient(160deg,#5a7a6a,#8aa0a0 50%,#a090b0);
  --photo-crowd:radial-gradient(ellipse at 30% 40%,rgba(120,80,50,.5),transparent 40%),radial-gradient(ellipse at 75% 35%,rgba(120,80,50,.45),transparent 40%),linear-gradient(120deg,#1e1510,#3a2a1e 50%,#1a120e);
  --photo-portrait:radial-gradient(circle at 50% 40%,#e0b898 0 30%,transparent 32%),linear-gradient(180deg,#9ab8d8,#d8c8c0);
}
*{margin:0;padding:0;box-sizing:border-box}
html,body{width:720px;height:1200px;overflow:hidden;background:var(--stage)}
.canvas{position:relative;width:720px;height:1200px;font-family:var(--sans);color:var(--white)}
.abs{position:absolute}
.ph{position:absolute;overflow:hidden}
.frame{position:absolute;background:var(--black)}
.brand{position:absolute;display:flex;align-items:center;gap:3px;font-family:var(--serif);font-weight:700;color:var(--gold);line-height:1.1;white-space:nowrap}
.brand .dot{border-radius:50%;background:var(--gold);flex:none}
.serif{font-family:var(--serif);font-weight:700}
.pill{position:absolute;border-radius:20px;display:flex;align-items:center;justify-content:center;font-weight:700;text-transform:uppercase;color:var(--white)}
.pill.gold{background:var(--gold)}
.pill.cyan{background:var(--cyan)}
.ring{position:absolute;border:1px solid var(--gold);border-radius:50%}
.field{position:absolute;background:var(--field);color:#cfcfcf;font-size:3px;padding:1.5px 3px}
.nav{position:absolute;left:158px;top:145.5px;width:286px;height:10.5px;background:var(--blue);display:flex;align-items:center;font-size:3px;font-weight:700;text-transform:uppercase;white-space:nowrap}
.nav span{padding:0 4px}
.nav .sep{padding:0 1px;color:#cfe4ff}
.nav .book{margin-left:auto;background:var(--orange);height:100%;width:41px;display:flex;align-items:center;justify-content:center;padding:0}
.card-label{position:absolute;left:0;right:0;text-align:center;font-family:var(--serif);font-weight:700;white-space:nowrap}
.service-title{position:absolute;font-family:var(--serif);font-weight:700;text-align:center;line-height:1.2}
.icon-disc{position:absolute;border-radius:50%;background:var(--black);border:1px solid var(--gold);display:flex;align-items:center;justify-content:center}
.contact-line{position:absolute;display:flex;gap:3px;align-items:flex-start;line-height:1.35;white-space:nowrap}
.quote{position:absolute;text-align:center;font-style:italic;color:var(--muted)}
</style>
</head>
<body>
<div class="canvas">

<!-- ================= DESKTOP ================= -->
<div class="frame" style="left:96px;top:120px;width:410px;height:581px"></div>
<div class="abs" style="left:96px;top:701px;width:410px;height:112px;background:var(--panel)"></div>
<div class="frame" style="left:96px;top:959px;width:410px;height:121px"></div>

<!-- header -->
<div class="brand" style="left:158px;top:128px;font-size:5px"><span class="dot" style="width:8px;height:8px"></span><span>Bright Harbor<br>Concierge</span></div>
<div class="abs" style="left:280px;top:130px;font-size:4px;font-weight:700;display:flex;align-items:center;gap:2px;white-space:nowrap">
  <span style="color:var(--gold)">Custom Party Packages:</span>
  <svg width="4" height="4" viewBox="0 0 10 10"><path d="M2 1l2 2-1 1.5c.8 1.6 1.9 2.7 3.5 3.5L8 7l2 2-1.5 1C4.5 9.5.5 5.5 0 2.5z" fill="var(--gold)"/></svg>
  <span>555-014-7290</span>
</div>
<div class="ring" style="left:378px;top:127px;width:10px;height:10px"></div>
<div class="ring" style="left:392px;top:127px;width:10px;height:10px"></div>
<div class="abs" style="left:410px;top:128px;width:34px;height:10px;background:#5aa832;border-radius:1px"></div>

<nav class="nav">
  <span>Home</span><span class="sep">//</span><span>About Us</span><span class="sep">//</span><span>Services</span><span class="sep">//</span><span>Reviews</span><span class="sep">//</span><span>Nightlife</span><span class="sep">//</span><span>Gallery</span><span class="sep">//</span><span>Contact Us</span>
  <span class="book">Book Now</span>
</nav>

<!-- hero -->
<div class="ph" role="img" aria-label="Group of friends celebrating at a pool party" style="left:96px;top:156px;width:410px;height:138.5px;background:var(--photo-pool)"></div>
<div class="abs serif" style="left:158px;top:192px;width:185px;font-size:11px;line-height:12px;font-weight:400;text-shadow:0 0 4px rgba(0,0,0,.4)">Lorem Ipsum is simply<br>dummy text of the printing and<br>typesetting industry.</div>
<div class="pill cyan" style="left:158px;top:237px;width:34px;height:9.5px;font-size:3px">Contact Us</div>
<div class="abs" style="left:439px;top:205px;display:flex;flex-direction:column;gap:3px">
  <span class="ring" style="position:static;display:block;width:4px;height:4px;border-color:#fff"></span>
  <span style="display:block;width:4px;height:4px;border-radius:50%;background:#fff"></span>
  <span class="ring" style="position:static;display:block;width:4px;height:4px;border-color:#fff"></span>
  <span class="ring" style="position:static;display:block;width:4px;height:4px;border-color:#fff"></span>
</div>
<div class="abs" style="left:150px;top:278px;width:303px;height:17px;background:var(--black)"></div>

<!-- feature cards -->
<div class="ph" role="img" aria-label="Friends toasting at a bachelor party" style="left:158px;top:286px;width:92px;height:107px;background:var(--photo-bachelor)">
  <div class="card-label" style="top:91px;font-size:6.5px">Bachelor parties</div>
</div>
<div class="ph" role="img" aria-label="Women celebrating with champagne at a bachelorette party" style="left:255px;top:286px;width:92px;height:107px;background:var(--photo-bachelorette)">
  <div class="card-label" style="top:71px;font-size:6.5px">Bachelorette parties</div>
  <div class="pill gold" style="left:29px;top:86px;width:34px;height:9.5px;font-size:3px">Book Now</div>
</div>
<div class="ph" role="img" aria-label="Traveller resting beside a car" style="left:352px;top:286px;width:92px;height:107px;background:var(--photo-medical)">
  <div class="card-label" style="top:91px;font-size:6.5px">Medical tourism</div>
</div>

<!-- airport -->
<div class="ph" role="img" aria-label="Family walking through an airport terminal with luggage" style="left:158px;top:410px;width:140px;height:63px;background:var(--photo-airport)"></div>
<svg class="abs" style="left:272px;top:410px" width="123" height="63" viewBox="0 0 123 63"><polygon points="26,0 123,0 123,63 6,63" fill="var(--cyan)"/><polygon points="20,0 26,0 6,63 0,63" fill="#e0503a"/><polygon points="23,0 26,0 6,63 3,63" fill="var(--orange)"/></svg>
<div class="icon-disc" style="left:270px;top:427.5px;width:28px;height:28px">
  <svg width="13" height="13" viewBox="0 0 20 20"><path d="M2 11l16-5-2 4-9 3-3 3-1-1 1-2-2-2z" fill="var(--gold)"/></svg>
</div>
<div class="service-title" style="left:300px;top:430px;width:90px;font-size:9.5px">Airport<br>Transportation</div>
<div class="brand" style="left:403px;top:435px;font-size:5.5px"><span class="dot" style="width:5px;height:5px"></span><span>Bright Harbor<br>Concierge</span></div>

<!-- lodging -->
<div class="brand" style="left:158px;top:507px;font-size:5.5px"><span class="dot" style="width:5px;height:5px"></span><span>Bright Harbor<br>Concierge</span></div>
<div class="ph" role="img" aria-label="Traveller on the balcony of a wooden lodge" style="left:308px;top:482px;width:136px;height:62px;background:var(--photo-lodge)"></div>
<svg class="abs" style="left:207px;top:482px" width="123" height="62" viewBox="0 0 123 62"><polygon points="0,0 101,0 123,62 0,62" fill="var(--navy)"/><polygon points="101,0 106,0 123,50 123,62" fill="#e0503a"/></svg>
<div class="icon-disc" style="left:302px;top:499px;width:27px;height:27px">
  <svg width="12" height="12" viewBox="0 0 20 20"><path d="M10 2l8 7h-2v9H4V9H2z" fill="var(--gold)"/><rect x="8" y="12" width="4" height="6" fill="#000"/></svg>
</div>
<div class="service-title" style="left:218px;top:506px;width:80px;font-size:9.5px">Lodging</div>

<!-- bilingual -->
<div class="ph" role="img" aria-label="Tour group with a guide in front of a historic tower" style="left:158px;top:553px;width:140px;height:63px;background:var(--photo-tour)"></div>
<svg class="abs" style="left:272px;top:553px" width="123" height="63" viewBox="0 0 123 63"><polygon points="26,0 123,0 123,63 6,63" fill="var(--teal)"/><polygon points="20,0 26,0 6,63 0,63" fill="#e0503a"/><polygon points="23,0 26,0 6,63 3,63" fill="var(--orange)"/></svg>
<div class="icon-disc" style="left:270px;top:570.5px;width:28px;height:28px">
  <svg width="12" height="12" viewBox="0 0 20 20"><rect x="3" y="2" width="11" height="15" fill="var(--gold)"/><circle cx="15" cy="15" r="4" fill="var(--gold)" stroke="#000"/></svg>
</div>
<div class="service-title" style="left:300px;top:573px;width:90px;font-size:9.5px">Bilingual<br>Guides</div>
<div class="brand" style="left:403px;top:578px;font-size:5.5px"><span class="dot" style="width:5px;height:5px"></span><span>Bright Harbor<br>Concierge</span></div>

<!-- special needs -->
<div class="abs serif" style="left:158px;top:632px;width:286px;text-align:center;font-size:6.5px;color:var(--gold)">Any other special needs?</div>
<div class="abs serif" style="left:158px;top:641px;width:286px;text-align:center;font-size:9.5px;color:var(--cyan)">Call now: 555-014-7290</div>

<!-- gallery -->
<div class="ph" role="img" aria-label="Friends drinking at a bar" style="left:158px;top:668px;width:68px;height:59px;background:var(--photo-bar)"></div>
<div class="ph" role="img" aria-label="Friends sharing a toast" style="left:158px;top:732px;width:68px;height:59px;background:var(--photo-toast)"></div>
<div class="ph" role="img" aria-label="Friends laughing at a house party" style="left:231px;top:668px;width:140px;height:123px;background:var(--photo-house)"></div>
<div class="ph" role="img" aria-label="Crowd dancing at a nightclub" style="left:376px;top:668px;width:68px;height:59px;background:var(--photo-club)"></div>
<div class="ph" role="img" aria-label="Group blowing confetti outdoors" style="left:376px;top:732px;width:68px;height:59px;background:var(--photo-confetti)"></div>

<!-- testimonials -->
<div class="ph" role="img" aria-label="Dim party crowd background" style="left:96px;top:813px;width:410px;height:146px;background:var(--photo-crowd)"></div>
<div class="abs serif" style="left:96px;top:832px;width:410px;text-align:center;font-size:9px;color:var(--cyan)">What our clients say</div>
<div class="ring" style="left:289px;top:852px;width:24px;height:24px"></div>
<div class="ph" role="img" aria-label="Client portrait" style="left:292px;top:855px;width:18px;height:18px;border-radius:50%;background:var(--photo-portrait)"></div>
<svg class="abs" style="left:164px;top:882px" width="6" height="8" viewBox="0 0 6 8"><path d="M5 0L1 4l4 4" stroke="#aaa" fill="none"/></svg>
<svg class="abs" style="left:432px;top:882px" width="6" height="8" viewBox="0 0 6 8"><path d="M1 0l4 4-4 4" stroke="#aaa" fill="none"/></svg>
<p class="quote" style="left:196px;top:879px;width:210px;font-size:3.2px;line-height:5px">There are many variations of passages of Lorem Ipsum available, but the majority have suffered alteration in some form, by injected humour, or randomised words which don't look even slightly believable. If you are going to use a passage of lorem Ipsum, you need to be sure there isn't anything embarrassing</p>
<div class="abs" style="left:96px;top:902px;width:410px;text-align:center;font-size:3.4px"><span style="color:var(--gold)">Avery Lane</span> / Loyal Customer</div>
<div class="pill cyan" style="left:284px;top:916px;width:34px;height:10px;font-size:3px">View All</div>

<!-- footer -->
<div class="abs serif" style="left:158px;top:980px;font-size:5.5px">Conatct Us</div>
<div class="contact-line" style="left:158px;top:993px;font-size:4.5px">
  <svg width="4" height="4" viewBox="0 0 10 10"><path d="M2 1l2 2-1 1.5c.8 1.6 1.9 2.7 3.5 3.5L8 7l2 2-1.5 1C4.5 9.5.5 5.5 0 2.5z" fill="var(--gold)"/></svg>(555) 014-9978</div>
<div class="contact-line" style="left:158px;top:1001px;font-size:3.4px">
  <svg width="4" height="3" viewBox="0 0 10 8"><rect x=".5" y=".5" width="9" height="7" fill="none" stroke="var(--gold)"/></svg>hello@brightharbor.example</div>
<div class="contact-line" style="left:158px;top:1011px;font-size:3.2px">
  <svg width="3" height="4" viewBox="0 0 8 10"><path d="M4 0a4 4 0 014 4c0 3-4 6-4 6S0 7 0 4a4 4 0 014-4z" fill="var(--gold)"/></svg><span>Lorem Mall Shopping Center,<br>1544 Ipsum work Ave NE., # 406, contry<br>Design - 12345</span></div>
<div class="ring" style="left:158px;top:1035px;width:10px;height:10px"></div>
<div class="ring" style="left:171px;top:1035px;width:10px;height:10px"></div>

<div class="abs serif" style="left:243px;top:980px;font-size:5.5px">Send Us Message</div>
<div class="field" style="left:243px;top:993px;width:64.5px;height:8px">Name</div>
<div class="field" style="left:312px;top:993px;width:64px;height:8px">Email</div>
<div class="field" style="left:380px;top:993px;width:64px;height:8px">Phone</div>
<div class="field" style="left:243px;top:1005px;width:201px;height:26px">Message</div>
<div class="pill gold" style="left:243px;top:1035px;width:30px;height:10.5px;font-size:3px">Send</div>

<div class="abs" style="left:158px;top:1057px;font-size:3.2px;white-space:nowrap">© 2021 <span style="color:var(--gold)">Bright Harbor Concierge</span>. All Rights Reserved.</div>
<svg class="abs" style="left:449px;top:1054px" width="7" height="8" viewBox="0 0 7 8"><polygon points="3.5,0 7,8 3.5,6 0,8" fill="var(--gold)"/></svg>

<!-- ================= MOBILE ================= -->
<div class="frame" style="left:526px;top:120px;width:97.5px;height:960px"></div>

<div class="brand" style="left:534px;top:127px;font-size:3.6px"><span class="dot" style="width:6px;height:6px"></span><span>Bright Harbor<br>Concierge</span></div>
<div class="abs" style="left:570px;top:130px;font-size:3.2px;font-weight:700;display:flex;gap:1px;align-items:center;white-space:nowrap">
  <svg width="3" height="3" viewBox="0 0 10 10"><path d="M2 1l2 2-1 1.5c.8 1.6 1.9 2.7 3.5 3.5L8 7l2 2-1.5 1C4.5 9.5.5 5.5 0 2.5z" fill="var(--gold)"/></svg>555-014-7290</div>
<div class="abs" style="left:605px;top:127px;width:10px;height:10px;border-radius:50%;background:var(--gold);display:flex;flex-direction:column;justify-content:center;align-items:center;gap:1px">
  <span style="width:5px;height:.7px;background:#000"></span><span style="width:5px;height:.7px;background:#000"></span><span style="width:5px;height:.7px;background:#000"></span>
</div>

<div class="ph" role="img" aria-label="Group of friends celebrating at a pool party" style="left:526px;top:144px;width:97.5px;height:61px;background:var(--photo-pool)"></div>
<div class="abs serif" style="left:530px;top:157px;width:90px;text-align:center;font-size:5px;font-weight:400;line-height:7px">Lorem Ipsum is simply<br>dummy text of the printing and<br>typesetting industry.</div>
<div class="pill gold" style="left:558.5px;top:183.5px;width:32.5px;height:7.5px;font-size:2.6px">Contact Us</div>

<div class="ph" role="img" aria-label="Friends toasting at a bachelor party" style="left:534px;top:205px;width:81px;height:95px;background:var(--photo-bachelor)">
  <div class="card-label" style="top:84px;font-size:5px">Bachelor parties</div>
</div>
<div class="ph" role="img" aria-label="Women celebrating with champagne at a bachelorette party" style="left:534px;top:304px;width:81px;height:95px;background:var(--photo-bachelorette)">
  <div class="card-label" style="top:67px;font-size:5px">Bachelorette parties</div>
  <div class="pill gold" style="left:24.5px;top:78px;width:32px;height:7.5px;font-size:2.6px">Book Now</div>
</div>
<div class="ph" role="img" aria-label="Traveller resting beside a car" style="left:534px;top:403px;width:81px;height:94px;background:var(--photo-medical)">
  <div class="card-label" style="top:84px;font-size:5px">Medical tourism</div>
</div>

<!-- mobile services -->
<div class="ph" role="img" aria-label="Family walking through an airport terminal" style="left:526px;top:506px;width:52px;height:51px;background:var(--photo-airport)"></div>
<svg class="abs" style="left:566px;top:506px" width="57.5" height="51" viewBox="0 0 57.5 51"><polygon points="16,0 57.5,0 57.5,51 4,51" fill="var(--cyan)"/><polygon points="12,0 16,0 4,51 0,51" fill="#e0503a"/></svg>
<div class="icon-disc" style="left:564px;top:522px;width:18px;height:18px"><svg width="9" height="9" viewBox="0 0 20 20"><path d="M2 11l16-5-2 4-9 3-3 3-1-1 1-2-2-2z" fill="var(--gold)"/></svg></div>
<div class="service-title" style="left:582px;top:525px;width:41px;font-size:4.4px">Airport<br>Transportation</div>

<div class="ph" role="img" aria-label="Traveller on the balcony of a wooden lodge" style="left:574px;top:562px;width:49.5px;height:51px;background:var(--photo-lodge)"></div>
<svg class="abs" style="left:526px;top:562px" width="60" height="51" viewBox="0 0 60 51"><polygon points="0,0 46,0 58,51 0,51" fill="var(--navy)"/><polygon points="46,0 49,0 60,45 58,51" fill="#e0503a"/></svg>
<div class="icon-disc" style="left:567.5px;top:578.5px;width:18px;height:18px"><svg width="9" height="9" viewBox="0 0 20 20"><path d="M10 2l8 7h-2v9H4V9H2z" fill="var(--gold)"/></svg></div>
<div class="service-title" style="left:530px;top:584px;width:34px;font-size:4.4px">Lodging</div>

<div class="ph" role="img" aria-label="Tour group with a guide in front of a historic tower" style="left:526px;top:618px;width:52px;height:51px;background:var(--photo-tour)"></div>
<svg class="abs" style="left:566px;top:618px" width="57.5" height="51" viewBox="0 0 57.5 51"><polygon points="16,0 57.5,0 57.5,51 4,51" fill="var(--teal)"/><polygon points="12,0 16,0 4,51 0,51" fill="#e0503a"/></svg>
<div class="icon-disc" style="left:564px;top:634px;width:18px;height:18px"><svg width="9" height="9" viewBox="0 0 20 20"><path d="M2 11l16-5-2 4-9 3-3 3-1-1 1-2-2-2z" fill="var(--gold)"/></svg></div>
<div class="service-title" style="left:582px;top:637px;width:41px;font-size:4.4px">Bilingual<br>Guides</div>

<div class="abs serif" style="left:526px;top:676.5px;width:97.5px;text-align:center;font-size:4px;color:var(--gold)">Any other special needs?</div>
<div class="abs serif" style="left:526px;top:684px;width:97.5px;text-align:center;font-size:6px;color:var(--cyan)">Call now: 555-014-7290</div>

<div class="ph" role="img" aria-label="Friends laughing at a house party" style="left:530px;top:698px;width:89px;height:78px;background:var(--photo-house)"></div>
<div class="abs" style="left:567px;top:773px;width:7px;height:7px;border-radius:50%;background:var(--gold)"></div>
<div class="abs" style="left:577px;top:773px;width:7px;height:7px;border-radius:50%;background:var(--gold)"></div>
<div class="abs" style="left:526px;top:781px;width:97.5px;height:5px;background:var(--panel)"></div>

<div class="ph" role="img" aria-label="Dim party crowd background" style="left:526px;top:786px;width:97.5px;height:121px;background:var(--photo-crowd)"></div>
<div class="abs serif" style="left:526px;top:794px;width:97.5px;text-align:center;font-size:6px;color:var(--cyan)">What our clients say</div>
<div class="ring" style="left:563px;top:807px;width:23px;height:23px"></div>
<div class="ph" role="img" aria-label="Client portrait" style="left:566px;top:810px;width:17px;height:17px;border-radius:50%;background:var(--photo-portrait)"></div>
<p class="quote" style="left:532px;top:836px;width:86px;font-size:2.7px;line-height:4.9px">There are many variations of passages of Lorem Ipsum available, but the majority have suffered alteration in some form, by injected humour, or randomised words which don't look even slightly believable. If you are going to use a passage of lorem Ipsum, you need to be sure there isn't anything embarrassing</p>
<div class="abs" style="left:526px;top:879px;width:97.5px;text-align:center;font-size:2.9px"><span style="color:var(--gold)">Avery Lane</span> / Loyal Customer</div>
<div class="pill gold" style="left:558.5px;top:889px;width:32.5px;height:7.5px;font-size:2.6px">View All</div>

<div class="abs serif" style="left:534px;top:917px;font-size:4.6px">Conatct Us</div>
<div class="contact-line" style="left:534px;top:928px;font-size:3.6px"><svg width="3" height="3" viewBox="0 0 10 10"><path d="M2 1l2 2-1 1.5c.8 1.6 1.9 2.7 3.5 3.5L8 7l2 2-1.5 1C4.5 9.5.5 5.5 0 2.5z" fill="var(--gold)"/></svg>(555) 014-9978</div>
<div class="contact-line" style="left:534px;top:936.5px;font-size:2.8px"><svg width="3" height="3" viewBox="0 0 10 8"><rect x=".5" y=".5" width="9" height="7" fill="none" stroke="var(--gold)"/></svg>hello@brightharbor.example</div>
<div class="contact-line" style="left:534px;top:946px;font-size:2.7px"><svg width="3" height="3" viewBox="0 0 8 10"><path d="M4 0a4 4 0 014 4c0 3-4 6-4 6S0 7 0 4a4 4 0 014-4z" fill="var(--gold)"/></svg><span>Lorem Mall Shopping Center,<br>1544 Ipsum work Ave NE., # 406, contry<br>Design - 12345</span></div>
<div class="ring" style="left:534px;top:966px;width:9px;height:9px"></div>
<div class="ring" style="left:546px;top:966px;width:9px;height:9px"></div>

<div class="abs serif" style="left:534px;top:984px;font-size:4.6px">Send Us Message</div>
<div class="field" style="left:534px;top:997.5px;width:81px;height:7px;font-size:2.6px;padding:1px 2px">Name</div>
<div class="field" style="left:534px;top:1007.5px;width:81px;height:7px;font-size:2.6px;padding:1px 2px">Email</div>
<div class="field" style="left:534px;top:1018px;width:81px;height:7px;font-size:2.6px;padding:1px 2px">Phone</div>
<div class="field" style="left:534px;top:1028px;width:81px;height:18px;font-size:2.6px;padding:1px 2px">Message</div>
<div class="pill gold" style="left:534px;top:1048.5px;width:28px;height:7.5px;font-size:2.6px">Send</div>
<div class="abs" style="left:534px;top:1066px;font-size:2.6px;white-space:nowrap">© 2021 <span style="color:var(--gold)">Bright Harbor Concierge</span>. All Rights Reserved.</div>
<svg class="abs" style="left:611px;top:1065px" width="5" height="6" viewBox="0 0 7 8"><polygon points="3.5,0 7,8 3.5,6 0,8" fill="var(--gold)"/></svg>

</div>
</body>
</html>
```